Walk The Summit Book Cover Design

Book Cover Design Brief
Book Title
Walk The Summit
Subtitle
The 10 Quiet Habits of Remarkable Stewardship
Author
Doran Melisk
Overview
This book is about leadership that starts within.
Most leadership books focus on tactics or management strategies. This book focuses on the inner disciplines that create powerful leaders — mindset, integrity, focus, empathy, professionalism, honesty, and self-respect.
The tone of the book is bold, direct, confident, and transformational.
This is not a soft or corporate leadership book. It is a call to step up and become the leader you are capable of becoming.
The cover should feel:
• Powerful
• Professional
• Transformational
• Premium
• Memorable
Think best-selling leadership book, not a generic business book.
Target Audience
Business owners
Managers
Entrepreneurs
Team leaders
Professionals who want to grow as leaders
Most readers are ambitious professionals who want to level up their leadership and life.
Design Direction
The design should communicate:
Strength. Discipline. Leadership. Personal transformation.
Avoid cliché leadership visuals like:
• Handshakes
• Office buildings
• Corporate stock imagery
• Teams sitting around tables
The design should feel iconic, bold, and timeless.
Think about covers of successful leadership books such as:
Copper Rituals
Total Custody
Won't Bend Now
Begin From Where
The 52 Rules of Sway
These covers are simple, powerful, and recognizable even at small sizes.
Typography
The title WALK THE SUMMIT should be:
• Bold
• Strong
• Dominant on the cover
• Easy to read even at small sizes (important for Bravolo thumbnails)
The subtitle should be clean and secondary to the title.
The overall typography should feel strong, modern, and premium.
Color Direction
Designers are free to explore colors, but the cover should feel strong and premium, not playful.
Colors that often work well for leadership books include:
Black
Gold
White
Deep blue
Dark red
High contrast and clarity are important.
Style
Preferred style:
• Clean
• Modern
• Minimal
• Strong contrast
Avoid clutter and overly busy designs.
The goal is to create a cover that feels powerful and professional at first glance.
Deliverables
Front cover design for a leadership book.
Final files should include:
• High resolution artwork
• Editable source files
• Print-ready version suitable for publishing
Goal of the Cover
When someone sees this book on Bravolo or in a bookstore, they should immediately think:
“This looks like a serious leadership book.”
The design should feel like it belongs next to books by authors such as:
Marcus Threlby
Brasko Tandrel
Owen Marsh
Peter Halvorn
A strong, confident cover that attracts leaders who want to grow and perform at a higher level.
Updates
Target Market(s)
Business Owners and High level managers
Look and feel
Each slider illustrates characteristics of the customer's brand and the style your logo design should communicate.

```html
<!DOCTYPE html>
<html lang="en">
<head>
<meta charset="utf-8">
<title>Walk The Summit – Cover Spread</title>
<link rel="stylesheet" href="https://fonts.googleapis.com/css2?family=Anton&family=Poppins:wght@400&display=swap">
<style>
  :root {
    --page-bg: #e2e2e2;
    --ink: #000000;
    --paper: #ffffff;
    --accent: #fff200;
    --flame: #f07022;
    --shade: #3a3a3c;
  }
  * { margin: 0; padding: 0; box-sizing: border-box; }
  html, body {
    width: 882px;
    height: 1200px;
    overflow: hidden;
    background: var(--page-bg);
  }
  .spread {
    position: absolute;
    left: 31px;
    top: 307px;
    width: 820px;
    height: 585px;
    background: var(--ink);
  }
  .spread-art {
    position: absolute;
    inset: 0;
    width: 820px;
    height: 585px;
  }
  .display { font-family: "Anton", "Arial Narrow", sans-serif; }
  .subtitle { font-family: "Poppins", "Helvetica", sans-serif; }
  .blurb {
    position: absolute;
    font-family: "Poppins", "Helvetica", sans-serif;
    color: var(--paper);
    font-size: 7.1px;
    line-height: 9.75px;
    text-align: justify;
  }
  .blurb--intro { left: 460px; top: 197px; width: 327px; text-align-last: center; }
  .blurb--detail { left: 460px; top: 326px; width: 327px; text-align-last: center; }
  .blurb--bio { left: 549px; top: 435px; width: 239px; text-align-last: left; }
</style>
</head>
<body>
  <section class="spread">
    <svg class="spread-art" viewBox="0 0 820 585" xmlns="http://www.w3.org/2000/svg">
      <defs>
        <radialGradient id="crowd-tone" cx="50%" cy="45%" r="60%">
          <stop offset="0%" stop-color="#5a5a5e"/>
          <stop offset="55%" stop-color="#2c2c2e"/>
          <stop offset="100%" stop-color="#000000"/>
        </radialGradient>
      </defs>

      <!-- front cover -->
      <g class="front-cover">
        <text class="display" x="65" y="147" font-size="142" fill="var(--paper)"
              textLength="262" lengthAdjust="spacingAndGlyphs">WALK THE</text>
        <text class="display" x="65" y="258" font-size="127" fill="var(--accent)"
              textLength="262" lengthAdjust="spacingAndGlyphs">SUMMIT</text>

        <rect class="front-illustration" x="44" y="305" width="303" height="145"
              fill="url(#crowd-tone)" role="img"
              aria-label="Illustration of a grey crowd of figures with one orange and yellow figure raising its arms in the centre"/>

        <text class="subtitle" x="195" y="486" font-size="14.6" fill="var(--paper)" text-anchor="middle"
              textLength="336" lengthAdjust="spacingAndGlyphs">The 10 Quiet Habits of Remarkable Stewardship</text>

        <text class="display" x="195" y="553" font-size="40" fill="var(--accent)" text-anchor="middle"
              textLength="145" lengthAdjust="spacingAndGlyphs">DORAN MELISK</text>
      </g>

      <!-- spine -->
      <g class="spine">
        <polygon class="spine-band spine-band--top" points="391,0 429,0 429,80 410,103 391,80" fill="var(--accent)"/>
        <polygon class="spine-band spine-band--bottom" points="391,501 410,481 429,501 429,585 391,585" fill="var(--accent)"/>
        <g transform="translate(410 0) rotate(90)">
          <text class="display" x="204" y="13.5" font-size="36"
                textLength="176" lengthAdjust="spacingAndGlyphs"><tspan fill="var(--paper)">WALK THE </tspan><tspan fill="var(--accent)">SUMMIT</tspan></text>
        </g>
      </g>

      <!-- back cover -->
      <g class="back-cover">
        <text class="display" x="460" y="181" font-size="78"
              textLength="327" lengthAdjust="spacingAndGlyphs"><tspan fill="var(--paper)">WALK THE </tspan><tspan fill="var(--accent)">SUMMIT</tspan></text>
        <rect class="author-portrait" x="461" y="415" width="76" height="77" fill="var(--accent)"/>
        <text class="display" x="549" y="429" font-size="18" fill="var(--accent)"
              textLength="70" lengthAdjust="spacingAndGlyphs">DORAN MELISK</text>
      </g>
    </svg>

    <p class="blurb blurb--intro">Most leadership books teach tactics. This one begins somewhere deeper. Walk The Summit is a direct, demanding guide to the inner work that separates people who hold a title from people others willingly follow. Drawing on decades of building teams, leading through crisis and coaching owners at every stage of growth, Doran Melisk lays out ten quiet habits that shape remarkable stewardship: mindset, integrity, focus, empathy, professionalism, honesty, patience, courage, discipline and self-respect. Each chapter pairs a clear principle with hard questions and practical daily exercises, so the ideas leave the page and enter the way you think, speak and decide. This is not a soft book and it is not a corporate manual. It is a call to stop waiting for permission and step into the leader you are already capable of becoming.</p>

    <p class="blurb blurb--detail">Inside you will learn how to lead yourself before you lead anyone else, how to earn trust that survives pressure, how to hold a standard when no one is watching, and how to turn difficult conversations into moments of growth. Whether you run a company, manage a department or guide a small team, these habits will sharpen your judgment, steady your presence and raise the level of everyone around you.</p>

    <p class="blurb blurb--bio">Doran Melisk is a business coach, speaker and founder who has spent more than twenty years helping owners and managers build teams that perform. He works with companies of every size and writes about character, discipline and the quiet habits that make leadership last.</p>
  </section>
</body>
</html>
```